Visitenkarten für Erstellung von Beleihungswert- und Verkehrswertgutachten.
Zielgruppe
Ich erstelle Beleihungswert- und Verkehrswertgutachten.
Meine Zielgruppe sind alle Immobilieneigentümer, Kaufinteressenten, Erben von Immobilienvermögen evtl. auch Anwälte, Steuerberater.
Aufgabenstellung
Der Fokus liegt auf der Wertermittlung von Immobilien

```html
<!DOCTYPE html>
<html lang="de">
<head>
<meta charset="utf-8">
<title>Visitenkarte – Varen Immobilien Bewertung</title>
<link rel="stylesheet" href="https://fonts.googleapis.com/css2?family=Saira:wght@400;500;600&display=swap">
<style>
  :root {
    --navy: #1b1847;
    --magenta: #e0067f;
    --white: #ffffff;
    --ink: #111111;
    --page: #ffffff;
    --edge: #e4e4ea;
  }
  * { box-sizing: border-box; margin: 0; padding: 0; }
  html, body {
    width: 1200px;
    height: 1194px;
    overflow: hidden;
    background: var(--page);
    font-family: "Saira", "Arial Narrow", sans-serif;
  }
  .canvas { position: relative; width: 1200px; height: 1194px; }

  .card {
    position: absolute;
    width: 464px;
    height: 303px;
    overflow: hidden;
  }

  /* Front */
  .card-front {
    left: 164px;
    top: 272px;
    background: var(--navy);
    color: var(--white);
  }
  .brand {
    position: absolute;
    left: 0; right: 0;
    top: 104px;
    display: flex;
    flex-direction: column;
    align-items: center;
  }
  .brand-row { display: flex; align-items: center; gap: 12px; }
  .brand-square {
    width: 12px; height: 12px;
    background: var(--magenta);
  }
  .brand-name {
    font-size: 58px;
    font-weight: 500;
    line-height: 1;
    letter-spacing: 2px;
    color: var(--white);
  }
  .brand-tagline {
    margin-top: 6px;
    font-size: 15px;
    font-weight: 500;
    color: var(--white);
  }

  /* Back */
  .card-back {
    left: 533px;
    top: 648px;
    background: var(--white);
    border: 1px solid var(--edge);
  }
  .accent-bar {
    position: absolute;
    width: 8px;
    height: 46px;
    background: var(--magenta);
  }
  .accent-bar--left { left: 0; top: 84px; }
  .accent-bar--mid { left: 188px; top: 84px; width: 5px; }
  .person {
    position: absolute;
    left: 42px;
    top: 80px;
    color: var(--ink);
  }
  .person-name { font-size: 24px; font-weight: 500; line-height: 1.2; }
  .person-role { font-size: 13px; font-weight: 400; margin-top: 2px; }
  .contact {
    position: absolute;
    left: 212px;
    top: 80px;
    font-size: 14px;
    line-height: 1.22;
    color: var(--ink);
  }
  .credentials {
    position: absolute;
    left: 0; right: 0; bottom: 0;
    height: 109px;
    background: var(--navy);
    color: var(--white);
    padding: 20px 20px 0 42px;
    font-size: 10.4px;
    line-height: 1.3;
    font-weight: 500;
  }
</style>
</head>
<body>
<main class="canvas">
  <section class="card card-front" aria-label="Vorderseite">
    <div class="brand">
      <div class="brand-row">
        <span class="brand-square"></span>
        <span class="brand-name">VAREN</span>
      </div>
      <p class="brand-tagline">Varen Immobilien Bewertung</p>
    </div>
  </section>

  <section class="card card-back" aria-label="Rückseite">
    <span class="accent-bar accent-bar--left"></span>
    <div class="person">
      <p class="person-name">Lena Varen</p>
      <p class="person-role">Geschäftsführer</p>
    </div>
    <span class="accent-bar accent-bar--mid"></span>
    <address class="contact" style="font-style: normal;">
      Lindenhof-Weg 4/2<br>
      71999 Musterfeld<br>
      Mobil: 0176 5550182
    </address>
    <div class="credentials">
      DIN ISO/IEC 17024 zertifizierte Bau-Sachverständige für die Markt-<br>
      und Beleihungswertermittlung von Wohn- und Gewerbeimmobilie<br>
      ZERTIA D1,D3 und D3 zertifiziert<br>
      SIGEKO = Sicherheits- und Gesundheitsschutz-Koordinator für Baustellen.
    </div>
  </section>
</main>
</body>
</html>
```